Business Card Design

We recently had a new logo designed by Pixel Harbor. Now we want to create new business cards and letterhead that compliment our new logo.

We are audiologists in private practice specializing in hearing evaluations and fitting hearing aids. We want a clean and professional card.

We need business cards for each audiologist. The names and titles are:
Marnie Ostrova, AuD
Audiologist

Jen Tarbel, AuD
Audiologist

Corvina Plesk, AuD
Audiologist

We also need a business card with no provider. Just a generic one.

Finally, we need an appointment card. This is what the front desk uses to give to the patient with their next appointment date and time.

Target Market(s)

Our clients tend to be highly educated. They are older so the cards should be clean and easy to read. No squirrely font please.

Industry/Entity Type

Business

Contact Information for Business Card

20731 8th Ave NE, suite 417
Seattle, WA 98177
206-592-8074

Requirements
Must have
• Clean
Easy to read
Professional
Modern but approachable / warm
Should not have
• Other pictures besides the logo

```html
<!DOCTYPE html>
<html lang="en">
<head>
<meta charset="utf-8">
<title>Larchmont Hearing Services – Business &amp; Appointment Cards</title>
<link rel="stylesheet" href="https://fonts.googleapis.com/css2?family=Lato:wght@400;700;900&display=swap">
<style>
  :root {
    --stage: #2b2b2b;
    --teal: #3aa996;
    --teal-deep: #2d8f7f;
    --navy: #1c3a5c;
    --ink: #1f2a2a;
    --grey: #4a4a4a;
    --paper: #ffffff;
    --paper-shade: #eeeeee;
  }
  * { box-sizing: border-box; margin: 0; padding: 0; }
  html, body {
    width: 1200px; height: 873px; overflow: hidden;
    background: var(--stage);
    font-family: "Lato", Arial, sans-serif;
  }
  .stage {
    position: relative; width: 1200px; height: 873px;
    display: flex; align-items: center; justify-content: center; gap: 60px;
  }
  .card {
    position: relative; width: 500px; height: 286px;
    border-radius: 16px; overflow: hidden;
  }

  /* Appointment card */
  .appointment-card {
    background: var(--teal);
    color: var(--ink);
    padding: 22px 34px;
    font-weight: 700;
  }
  .appointment-card .title {
    text-align: center; font-size: 15px; letter-spacing: .5px;
    color: var(--paper);
    border-top: 2px solid var(--ink);
    padding-top: 12px;
  }
  .appointment-card .title span {
    border-bottom: 2px solid var(--paper); padding-bottom: 2px;
  }
  .field-line { border-bottom: 2px solid var(--ink); height: 26px; }
  .field-label {
    text-align: center; font-size: 13px; color: var(--paper); margin-top: 4px;
  }
  .days {
    display: flex; justify-content: space-between; margin-top: 14px;
    font-size: 13px; color: var(--paper);
  }
  .check { display: flex; align-items: center; gap: 5px; }
  .check i {
    display: inline-block; width: 16px; height: 16px;
    border: 2px solid var(--ink); border-radius: 3px;
  }
  .write-row {
    display: flex; align-items: flex-end; gap: 8px; margin-top: 16px;
    font-size: 14px; color: var(--paper);
  }
  .write-row .blank { flex: 1; border-bottom: 2px solid var(--ink); height: 18px; }
  .write-row .check { font-size: 13px; }
  .notes { margin-top: 16px; font-size: 13px; color: var(--paper); opacity: .85; }
  .notes .blank { border-bottom: 2px solid var(--ink); height: 20px; }

  /* Business card */
  .business-card {
    background: linear-gradient(160deg, var(--paper) 60%, var(--paper-shade));
  }
  .brand {
    position: absolute; top: 38px; right: 28px;
    display: flex; align-items: center; gap: 10px;
  }
  .brand-dot {
    width: 38px; height: 38px; border-radius: 50%; background: var(--navy);
  }
  .brand-name {
    font-weight: 900; font-size: 20px; color: var(--navy);
    letter-spacing: .5px; line-height: 1.05; text-transform: uppercase;
  }
  .rule {
    position: absolute; left: 200px; right: 20px; top: 142px;
    height: 2px; background: var(--teal);
  }
  .provider { position: absolute; left: 26px; top: 150px; }
  .provider-name { font-weight: 900; font-size: 20px; color: var(--teal); }
  .provider-title { font-weight: 700; font-size: 15px; color: var(--grey); margin-top: 2px; }
  .address {
    position: absolute; right: 24px; top: 156px; text-align: right;
    font-weight: 700; font-size: 14px; color: var(--navy); line-height: 1.35;
  }
  .contacts {
    position: absolute; left: 26px; top: 210px; list-style: none;
    font-weight: 700; font-size: 13px; color: var(--ink);
  }
  .contacts li { display: flex; align-items: center; gap: 10px; height: 23px; }
  .contacts svg { width: 16px; height: 16px; fill: none; stroke: var(--teal); stroke-width: 2; }
  .contacts svg .solid { fill: var(--teal); stroke: none; }
</style>
</head>
<body>
<main class="stage">

  <section class="card appointment-card" aria-label="Appointment card">
    <p class="title"><span>APPOINTMENT CARD</span></p>
    <div class="field-line"></div>
    <p class="field-label">Patient Name</p>
    <div class="days">
      <span class="check">Mon <i></i></span>
      <span class="check">Tue <i></i></span>
      <span class="check">Wed <i></i></span>
      <span class="check">Thu <i></i></span>
      <span class="check">Fri <i></i></span>
      <span class="check">Sat <i></i></span>
    </div>
    <div class="write-row">
      <span>Date:</span><span class="blank"></span>
    </div>
    <div class="write-row">
      <span>Time:</span><span class="blank"></span>
      <span class="check">AM <i></i></span>
      <span class="check">PM <i></i></span>
    </div>
    <div class="notes">
      <span>Notes:</span>
      <div class="blank"></div>
    </div>
  </section>

  <section class="card business-card" aria-label="Business card">
    <div class="brand">
      <span class="brand-dot"></span>
      <span class="brand-name">Larchmont<br>Hearing Services</span>
    </div>
    <div class="rule"></div>
    <div class="provider">
      <p class="provider-name">Marnie Ostrova, AuD</p>
      <p class="provider-title">Audiologist</p>
    </div>
    <p class="address">20731 8th Avenue NE, Suite 417<br>Seattle WA 98177</p>
    <ul class="contacts">
      <li>
        <svg viewBox="0 0 16 16" aria-hidden="true"><rect x="4" y="1" width="8" height="14" rx="1.5"/></svg>
        (206) 592-8074
      </li>
      <li>
        <svg viewBox="0 0 16 16" aria-hidden="true"><rect class="solid" x="1" y="6" width="14" height="6" rx="1"/><rect x="4" y="2" width="8" height="4"/><rect x="4" y="10" width="8" height="4"/></svg>
        206-592-8075
      </li>
      <li>
        <svg viewBox="0 0 16 16" aria-hidden="true"><rect class="solid" x="1" y="3" width="14" height="10" rx="1"/><path d="M1.5 3.5 8 9l6.5-5.5" stroke="#fff"/></svg>
        info@larchmonthearing.com
      </li>
    </ul>
  </section>

</main>
</body>
</html>
```